Criação de Papelaria (6 itens) para Logística, Entrega & Armazenamento
A empresa queria:
" Trabalhamos no seguinte de logística, no qual engloba diversos seguimentos, como armazenagem, transporte , manuseio e entregas. Nosso foco é o atendimento personalizado ao cliente, suprindo toda a demanda e necessidade do cliente sem ocasionar nenhum transtorno ao mesmo. "

```html
<!DOCTYPE html>
<html lang="pt-BR">
<head>
<meta charset="utf-8">
<title>Assinatura de e-mail – Vertex Soluções Logísticas</title>
<link href="https://fonts.googleapis.com/css2?family=Montserrat:wght@400;500;600;700&display=swap" rel="stylesheet">
<style>
  :root {
    --brand-red: #c4232b;
    --brand-red-dark: #a81a22;
    --ink: #4a4a4a;
    --ink-soft: #7a7a7a;
    --paper: #ffffff;
    --backdrop: #ececec;
  }
  * { box-sizing: border-box; margin: 0; padding: 0; }
  html, body { width: 1200px; height: 1200px; overflow: hidden; }
  body {
    background: var(--backdrop);
    font-family: "Montserrat", Arial, sans-serif;
    display: flex;
    align-items: center;
    justify-content: center;
  }
  .signature {
    position: relative;
    width: 1080px;
    height: 260px;
    background: var(--paper);
    display: flex;
    overflow: hidden;
  }
  .signature__brand {
    position: relative;
    width: 600px;
    height: 100%;
    background: var(--brand-red);
    clip-path: polygon(0 0, 100% 0, 88% 100%, 0 100%);
    display: flex;
    align-items: center;
    padding-left: 48px;
  }
  .brand-name {
    display: flex;
    flex-direction: column;
    color: var(--paper);
  }
  .brand-name__word {
    font-weight: 600;
    font-size: 52px;
    letter-spacing: 4px;
    line-height: 1;
    display: flex;
    align-items: center;
    gap: 16px;
  }
  .brand-name__mark {
    width: 22px;
    height: 22px;
    background: var(--paper);
  }
  .brand-name__tagline {
    font-size: 15px;
    font-weight: 600;
    letter-spacing: 6px;
    margin-top: 10px;
  }
  .signature__person {
    width: 220px;
    padding: 36px 0 0 24px;
  }
  .person__name {
    color: var(--brand-red);
    font-weight: 700;
    font-size: 16px;
    letter-spacing: 1px;
    text-transform: uppercase;
  }
  .person__role {
    color: var(--ink);
    font-size: 13px;
    margin-top: 4px;
  }
  .person__phone {
    display: flex;
    align-items: center;
    gap: 10px;
    color: var(--ink);
    font-size: 14px;
    margin-top: 26px;
  }
  .signature__contacts {
    flex: 1;
    padding: 30px 28px 0 0;
    display: flex;
    flex-direction: column;
    align-items: flex-end;
    gap: 9px;
  }
  .contact {
    display: flex;
    align-items: center;
    gap: 16px;
    color: var(--ink);
    font-size: 13.5px;
    text-align: right;
  }
  .contact--address { margin-top: 18px; line-height: 1.45; font-size: 12.5px; }
  .icon { width: 16px; height: 16px; flex: none; fill: var(--brand-red); }
</style>
</head>
<body>
  <section class="signature" aria-label="Assinatura de e-mail">
    <div class="signature__brand">
      <div class="brand-name">
        <span class="brand-name__word"><span class="brand-name__mark"></span>VERTEX</span>
        <span class="brand-name__tagline">SOLUÇÕES LOGÍSTICAS</span>
      </div>
    </div>

    <div class="signature__person">
      <p class="person__name">Renato Alves Prado</p>
      <p class="person__role">Cargo/Função</p>
      <p class="person__phone">
        <svg class="icon" viewBox="0 0 24 24"><path d="M6.6 10.8a15.1 15.1 0 0 0 6.6 6.6l2.2-2.2a1 1 0 0 1 1-.25 11.4 11.4 0 0 0 3.6.57 1 1 0 0 1 1 1V20a1 1 0 0 1-1 1A17 17 0 0 1 3 4a1 1 0 0 1 1-1h3.5a1 1 0 0 1 1 1c0 1.25.2 2.45.57 3.57a1 1 0 0 1-.25 1z"/></svg>
        (31) 3000-4455
      </p>
    </div>

    <div class="signature__contacts">
      <p class="contact">(31) 90000-1234
        <svg class="icon" viewBox="0 0 24 24"><path d="M6.6 10.8a15.1 15.1 0 0 0 6.6 6.6l2.2-2.2a1 1 0 0 1 1-.25 11.4 11.4 0 0 0 3.6.57 1 1 0 0 1 1 1V20a1 1 0 0 1-1 1A17 17 0 0 1 3 4a1 1 0 0 1 1-1h3.5a1 1 0 0 1 1 1c0 1.25.2 2.45.57 3.57a1 1 0 0 1-.25 1z"/></svg>
      </p>
      <p class="contact">(31) 90000-1234
        <svg class="icon" viewBox="0 0 24 24"><circle cx="12" cy="12" r="9"/></svg>
      </p>
      <p class="contact">contato@vertexlog.com.br
        <svg class="icon" viewBox="0 0 24 24"><path d="M2 5h20v14H2z"/><path d="M2 5l10 8 10-8" fill="none" stroke="#fff" stroke-width="2"/></svg>
      </p>
      <p class="contact">www.vertexlog.com.br
        <svg class="icon" viewBox="0 0 24 24"><circle cx="12" cy="12" r="9" fill="none" stroke="#c4232b" stroke-width="2"/><path d="M3 12h18M12 3c3 3 3 15 0 18M12 3c-3 3-3 15 0 18" fill="none" stroke="#c4232b" stroke-width="1.6"/></svg>
      </p>
      <p class="contact contact--address">Av. das Cargas, Nº 120 - Centro<br>Cidade/UF CEP: 30000-000
        <svg class="icon" viewBox="0 0 24 24"><path d="M12 2a7 7 0 0 0-7 7c0 5.2 7 13 7 13s7-7.8 7-13a7 7 0 0 0-7-7zm0 9.5A2.5 2.5 0 1 1 12 6.5a2.5 2.5 0 0 1 0 5z"/></svg>
      </p>
    </div>
  </section>
</body>
</html>
```